house selling company website

i need a website that is to get customers to let us sell their house within 30 days with no sales fees based in the uk. iv uploaded a design i like for the website i own i want a copy of this but for the different logo ect need the house buying logo i own to be changed to house selling company
it needs to be able to flash up to sell your house today contact box to collect their details such as property type, address, number of bedrooms, (estate agents valuation) , best price you can accept after they have seen the main section banner with advertising why use us.
the three reasons in the banner to use us needs to be
1: We will sell your house in 30 days and ensure we take a buyers fee for our service from the buyer meaning your buyer is secured unlike with most estate agents
2: We do not charge you any fees at all! our small fee is charged to the buyer
3: A huge network of investors and private buyers connecting many estate agents, auction houses, investors, and private buyers to ensure a fast sale.

```html
<!DOCTYPE html>
<html lang="en">
<head>
<meta charset="utf-8">
<title>SwiftSale Homes</title>
<link rel="stylesheet" href="https://fonts.googleapis.com/css2?family=Questrial&family=Quicksand:wght@500;600;700&display=swap">
<style>
:root{
  --night:#0d1440;
  --night-deep:#070b2a;
  --brand:#1e8fd3;
  --brand-dark:#2d6bc4;
  --slate:#4e4f55;
  --ink:#1d1d1f;
  --muted:#555;
  --card:#f6f6f6;
  --footer:#0b2540;
  --white:#fff;
}
*{box-sizing:border-box;margin:0;padding:0}
html,body{width:904px;height:1200px;overflow:hidden;background:var(--white)}
body{position:relative;font-family:"Questrial",sans-serif;color:var(--ink)}
.abs{position:absolute}

/* hero */
.hero{left:0;top:0;width:904px;height:580px;background:linear-gradient(180deg,var(--night-deep) 0%,var(--night) 55%,#1f2a66 100%)}
.brand{display:flex;align-items:center;gap:8px}
.brand-dot{width:26px;height:26px;border-radius:50%;background:var(--brand)}
.brand-name{font-family:"Quicksand",sans-serif;font-weight:600;font-size:19px;color:var(--brand)}
.hero .brand{left:89px;top:60px}
.btn{display:flex;align-items:center;justify-content:center;gap:5px;border-radius:4px;color:var(--white);font-size:10.5px}
.btn-login{left:658px;top:40px;width:69px;height:25px;background:var(--slate)}
.btn-register{left:735px;top:40px;width:78px;height:25px;background:var(--brand)}
.btn svg{width:9px;height:9px}
.hero-title{left:0;width:904px;top:163px;text-align:center;font-family:"Quicksand",sans-serif;font-weight:700;font-size:16px;color:var(--brand)}

/* sell today details form */
.valuation{left:180px;top:193px;width:543px;height:88px;background:var(--brand);border-radius:4px}
.field-label{top:13px;font-family:"Quicksand",sans-serif;font-weight:700;font-size:8px;color:var(--white);white-space:nowrap}
.field{top:27px;width:80px;height:24px;background:var(--white);border-radius:3px;font-size:8.5px;color:#888;display:flex;align-items:center;padding-left:8px;white-space:nowrap;overflow:hidden}
.caret{position:absolute;right:7px;top:10px;border-left:3px solid transparent;border-right:3px solid transparent;border-top:4px solid #444}
.btn-submit{left:462px;top:27px;width:61px;height:24px;background:var(--slate);border-radius:3px;color:var(--white);font-family:"Quicksand",sans-serif;font-weight:700;font-size:8px;letter-spacing:.5px;display:flex;align-items:center;justify-content:center}
.form-note{left:0;width:543px;top:62px;text-align:center;color:var(--white);font-size:11.5px}
.btn-info{left:336px;top:296px;width:232px;height:25px;background:var(--slate);border-radius:4px;color:var(--white);font-size:9.5px;display:flex;align-items:center;justify-content:center}
.neighbourhood{left:0;top:308px;width:904px;height:272px;background:linear-gradient(180deg,rgba(31,42,102,0) 0%,#3a3f7a 35%,#8c4a5c 70%,#9a9a3a 100%)}
.hero-rule{left:0;top:578px;width:904px;height:3px;background:var(--night)}

/* why choose */
.why-title{left:0;width:904px;top:641px;text-align:center;font-family:"Quicksand",sans-serif;font-weight:700;font-size:21px;color:var(--brand-dark)}
.why-sub{left:0;width:904px;top:668px;text-align:center;font-size:10.5px;color:var(--muted)}
.reason{top:719px;width:200px;height:163px;background:var(--card);border-radius:3px;box-shadow:0 1px 6px rgba(0,0,0,.1);text-align:center;font-size:10.5px;line-height:14px;color:var(--ink);padding:0 12px;display:flex;flex-direction:column;justify-content:center}
.reason-num{position:absolute;left:77px;top:-16px;width:46px;height:46px;border-radius:50%;background:var(--white);box-shadow:0 2px 4px rgba(0,0,0,.12);display:flex;align-items:center;justify-content:center}
.reason-num span{width:38px;height:38px;border-radius:50%;background:var(--brand);color:var(--white);font-family:"Quicksand",sans-serif;font-weight:700;font-size:16px;display:flex;align-items:center;justify-content:center}
.reason strong{display:block;font-family:"Quicksand",sans-serif;font-weight:700;font-size:11.5px;color:var(--brand-dark)}
.reason-1{left:131px}.reason-2{left:352px}.reason-3{left:573px}
.reason-1 .reason-body{margin-top:36px}
.reason-2 .reason-body{margin-top:6px;margin-bottom:20px}
.reason-3 .reason-body{margin-top:6px;margin-bottom:20px}
.reason-3 strong{color:var(--brand)}

/* footer */
.skyline{left:0;top:915px;width:904px;height:85px;background:linear-gradient(180deg,#ffffff 0%,#dfe2e7 35%,#1b3350 70%,var(--footer) 100%)}
.footer{left:0;top:998px;width:904px;height:176px;background:var(--footer);color:var(--white)}
.footer .brand{left:89px;top:94px}
.footer-head{font-family:"Quicksand",sans-serif;font-weight:700;font-size:11.5px;color:var(--brand)}
.contact{left:317px;top:42px}
.contact li{list-style:none;display:flex;align-items:center;gap:7px;font-size:9.5px;margin-top:12px}
.contact svg{width:10px;height:10px;fill:var(--brand)}
.links{top:42px}
.links li{list-style:none;font-size:9px;line-height:15.5px}
.links ul{margin-top:6px}
.links-quick{left:566px}.links-advice{left:690px}
.links .current{color:var(--brand);text-decoration:underline}
.bottom-bar{left:0;top:1174px;width:904px;height:26px;background:var(--brand);color:var(--white);font-size:8.5px}
.copyright{left:89px;top:8px}
.social{top:5px;width:16px;height:16px;border-radius:50%;background:var(--white)}
</style>
</head>
<body>

<header class="hero abs">
  <div class="brand abs"><span class="brand-dot"></span><span class="brand-name">SwiftSale Homes</span></div>
  <a class="btn btn-login abs"><svg viewBox="0 0 10 10" fill="none" stroke="#fff" stroke-width="1"><circle cx="5" cy="5" r="4"/><path d="M2.5 5h4M5 3.3 6.7 5 5 6.7"/></svg>Login</a>
  <a class="btn btn-register abs"><svg viewBox="0 0 10 10" fill="none" stroke="#fff" stroke-width="1"><circle cx="5" cy="3" r="2"/><path d="M1.5 9.5c0-2 1.6-3.5 3.5-3.5s3.5 1.5 3.5 3.5"/></svg>Register</a>

  <h1 class="hero-title abs">The Fastest way to sell your house, with no fees</h1>

  <form class="valuation abs">
    <label class="field-label abs" style="left:21px">Property type</label>
    <label class="field-label abs" style="left:109px">Address</label>
    <label class="field-label abs" style="left:197px">Bedrooms</label>
    <label class="field-label abs" style="left:285px">Agent valuation (£)</label>
    <label class="field-label abs" style="left:373px">Best price (£)</label>
    <div class="field abs" style="left:21px">Select<span class="caret"></span></div>
    <div class="field abs" style="left:109px">Post code</div>
    <div class="field abs" style="left:197px">Any<span class="caret"></span></div>
    <div class="field abs" style="left:285px">e.g. 250,000</div>
    <div class="field abs" style="left:373px">e.g. 240,000</div>
    <div class="btn-submit abs">SELL TODAY</div>
    <p class="form-note abs">Sell your house today, sold within 30 days</p>
  </form>

  <a class="btn-info abs">Selling your home? Click here for more info</a>

  <div class="neighbourhood abs" role="img" aria-label="Night-time street of houses with families and speech bubbles about moving home"></div>
  <div class="hero-rule abs"></div>
</header>

<section>
  <h2 class="why-title abs">Why Choose Us</h2>
  <p class="why-sub abs">The UK's fastest no-fee house selling service for homeowners</p>

  <article class="reason reason-1 abs">
    <div class="reason-num"><span>01</span></div>
    <p class="reason-body">We will<strong>SELL YOUR HOUSE IN 30 DAYS</strong>and ensure we take a buyers fee for our service from the buyer meaning your buyer is secured unlike with most estate agents</p>
  </article>
  <article class="reason reason-2 abs">
    <div class="reason-num"><span>02</span></div>
    <p class="reason-body"><strong>WE DO NOT CHARGE</strong>you any fees at all! our small fee is charged to the buyer</p>
  </article>
  <article class="reason reason-3 abs">
    <div class="reason-num"><span>03</span></div>
    <p class="reason-body"><strong>A HUGE NETWORK</strong>of investors and private buyers connecting many estate agents, auction houses, investors, and private buyers to ensure a fast sale.</p>
  </article>
</section>

<div class="skyline abs" role="img" aria-label="City skyline silhouette with clock tower and observation wheel"></div>

<footer class="footer abs">
  <div class="brand abs"><span class="brand-dot"></span><span class="brand-name">SwiftSale Homes</span></div>

  <div class="contact abs">
    <h3 class="footer-head">Contact Us</h3>
    <ul>
      <li><svg viewBox="0 0 10 10"><path d="M5 0a3.5 3.5 0 0 0-3.5 3.5C1.5 6 5 10 5 10s3.5-4 3.5-6.5A3.5 3.5 0 0 0 5 0zm0 5a1.4 1.4 0 1 1 0-2.8A1.4 1.4 0 0 1 5 5z"/></svg>27, Orchard Lane, Marlow, SL7 4QT</li>
      <li><svg viewBox="0 0 10 10"><path d="M2 0.5 3.6 2.6 2.8 3.8c.7 1.4 1.9 2.6 3.4 3.4l1.2-.8L9.5 8 8.3 9.5C4 9 1 6 .5 1.7z"/></svg>01-555-018-244</li>
      <li><svg viewBox="0 0 10 10"><path d="M0 2h10v6H0zm.8.7L5 5.6 9.2 2.7z" fill-rule="evenodd"/></svg>info@swiftsalehomes.co.uk</li>
    </ul>
  </div>

  <nav class="links links-quick abs">
    <h3 class="footer-head">Quick Links</h3>
    <ul><li class="current">Home</li><li>About</li><li>Accessibility</li><li>FAQ'S</li><li>Get in touch</li></ul>
  </nav>
  <nav class="links links-advice abs">
    <h3 class="footer-head">Advice &amp; tips</h3>
    <ul><li>Blog</li><li>Careers</li><li>Privacy</li><li>Terms</li></ul>
  </nav>
</footer>

<div class="bottom-bar abs">
  <p class="copyright abs">© 2023 Brightfield Digital Ltd. All Right Reserved</p>
  <span class="social abs" style="left:732px"></span>
  <span class="social abs" style="left:754px"></span>
  <span class="social abs" style="left:776px"></span>
  <span class="social abs" style="left:797px"></span>
</div>

</body>
</html>
```